Saffron Lantern Court Business Card

I am looking for a business card desgined for my restaurant. It is an Indian restaurant, we are looking for something thats modern, yet traditional with the indian culture, we are looking for colors that match our logo. The logo is a design of the building with the name of the restaurant. for more information on the restaurant go to www.saffronlanterncourt.example

Industry/Entity Type

Indian Restaurant

Contact Information for Business Card

we are looking for somthing thats modern, yet traditional with the indian culture, we are looking for colors that match our logo. The logo is a design of the building with the name of the restaurant. for more information on the restaurant go to www.saffronlanterncourt.example

Requirements
Must have
• The logo that is attached,
• Name: Harvinder Oberoi,
• address of the restaurant: 7328 West Larkspur Rd, Phoenix, Arizona, 85213
• Phone: (602) 555-0147
• Fax: (602) 555-0193
• Restaurant Catering Banquet
• Website: www.SaffronLanternCourt.example
Nice to have
• wanted to get something that goes with the theme of the restaurant, which is traditional but also keep a very professional and modern touch

```html
<!DOCTYPE html>
<html lang="en">
<head>
<meta charset="utf-8">
<title>Saffron Lantern Court – Business Card</title>
<link rel="stylesheet" href="https://fonts.googleapis.com/css2?family=Philosopher:wght@400;700&family=Arimo:wght@700&display=swap">
<style>
  :root {
    --page: #ffffff;
    --card-back: #ffffff;
    --card-edge: #ececec;
    --brand-red: #a8151b;
    --spice-deep: #9c2a0c;
    --spice-mid: #c4461a;
    --spice-light: #d9681f;
    --ink-light: #ffffff;
  }
  * { margin: 0; padding: 0; box-sizing: border-box; }
  html, body {
    width: 1200px; height: 1200px; overflow: hidden;
    background: var(--page);
  }
  .board { position: relative; width: 1200px; height: 1200px; }
  .card {
    position: absolute; left: 343px; width: 514px; height: 256px;
    overflow: hidden;
  }
  .card--front { top: 324px; }
  .card--back {
    top: 620px; background: var(--card-back);
    border: 1px solid var(--card-edge);
    text-align: center; color: var(--brand-red);
    font-family: "Philosopher", sans-serif;
  }
  .spice-photo {
    position: absolute; inset: 0;
    background:
      radial-gradient(ellipse 40% 45% at 88% 70%, var(--spice-light), transparent 70%),
      radial-gradient(ellipse 35% 30% at 70% 40%, var(--spice-light), transparent 70%),
      linear-gradient(100deg, var(--spice-mid) 0%, var(--spice-deep) 45%, var(--spice-mid) 100%);
  }
  .front-name {
    position: absolute; left: 0; right: 0; top: 50%;
    transform: translateY(-50%);
    text-align: center; color: var(--ink-light);
    font-family: "Philosopher", sans-serif; font-weight: 700;
    font-size: 40px; line-height: 1.05; letter-spacing: 1px;
    text-transform: uppercase;
  }
  .back-name {
    margin-top: 28px;
    font-weight: 700; font-size: 17px; line-height: 1.05;
    text-transform: uppercase; letter-spacing: .5px;
  }
  .person { margin-top: 30px; font-size: 13px; }
  .address { margin-top: 17px; font-size: 11px; }
  .contact-line { font-size: 13px; line-height: 16px; }
  .contact-line small { font-size: 8.5px; }
  .services { margin-top: 13px; font-size: 9px; }
  .website {
    font-family: "Arimo", sans-serif; font-weight: 700; font-size: 9.5px;
  }
</style>
</head>
<body>
<main class="board">
  <section class="card card--front">
    <div class="spice-photo" role="img" aria-label="Warm orange-toned photograph of bowls of ground spices and chillies on a wooden table"></div>
    <p class="front-name">Saffron<br>Lantern<br>Court</p>
  </section>

  <section class="card card--back">
    <p class="back-name">Saffron<br>Lantern<br>Court</p>
    <p class="person">Harvinder Oberoi</p>
    <p class="address">7328 West Larkspur Rd, Phoenix, Arizona, 85213</p>
    <p class="contact-line"><small>Phone:</small> (602) 555-0147</p>
    <p class="contact-line"><small>Fax:</small> (602) 555-0193</p>
    <p class="services">Restaurant Catering Banquet</p>
    <p class="website">www.SaffronLanternCourt.example</p>
  </section>
</main>
</body>
</html>
```